Amber Hollow Productions

I need a business card design for a new freelance film production company using or incorporating the logo:
I want the card to be creative, minimal, yet professional. Feel free to use a variety of different shapes and sizes/ textures for the card.

Industry/Entity Type

Film Production

```html
<!DOCTYPE html>
<html lang="en">
<head>
<meta charset="utf-8">
<title>Amber Hollow Productions – Business Cards</title>
<link href="https://fonts.googleapis.com/css2?family=Questrial&display=swap" rel="stylesheet">
<style>
  :root {
    --brand-blue: #0f55a8;
    --paper: #f1f1f2;
    --paper-shade: #e2e3e5;
    --ink-grey: #5a5a5a;
    --backdrop: #d9d9db;
    --white: #ffffff;
  }
  * { margin: 0; padding: 0; box-sizing: border-box; }
  html, body {
    width: 1200px; height: 1022px; overflow: hidden;
    background: var(--backdrop);
    font-family: "Questrial", "Century Gothic", sans-serif;
  }
  .canvas { position: relative; width: 1200px; height: 1022px; }

  .card {
    position: absolute;
    width: 700px; height: 400px;
    border-radius: 26px;
    overflow: hidden;
    box-shadow: 0 10px 30px rgba(0,0,0,0.18);
  }

  /* Back of card */
  .card-back {
    left: 70px; top: 70px;
    background: var(--brand-blue);
    color: var(--white);
  }
  .card-back .wordmark {
    position: absolute; left: 0; right: 0; top: 150px;
    display: flex; align-items: center; justify-content: center; gap: 16px;
  }
  .card-back .wordmark-square { width: 30px; height: 30px; background: var(--white); }
  .card-back .wordmark-name { font-size: 40px; letter-spacing: 1px; color: var(--white); white-space: nowrap; }
  .card-back .web {
    position: absolute; left: 0; right: 0; top: 290px;
    text-align: center; font-size: 20px; letter-spacing: 1px; white-space: nowrap;
  }

  /* Front of card */
  .card-front {
    left: 430px; top: 552px;
    background: linear-gradient(180deg, var(--white) 0%, var(--paper) 45%, var(--paper-shade) 100%);
  }
  .card-front .band {
    position: absolute; left: 0; right: 0; top: 150px; height: 120px;
    background: linear-gradient(90deg, rgba(255,255,255,0.6), rgba(255,255,255,0.2));
  }
  .card-front .corner-strip {
    position: absolute; left: 0; bottom: 0; width: 100%; height: 40px;
  }
  .card-front .wordmark {
    position: absolute; left: 40px; top: 172px;
    display: flex; align-items: center; gap: 12px;
  }
  .card-front .wordmark-square { width: 24px; height: 24px; background: var(--brand-blue); }
  .card-front .wordmark-name { font-size: 27px; color: var(--brand-blue); white-space: nowrap; }

  .contact-block { position: absolute; color: var(--brand-blue); white-space: nowrap; }
  .identity { left: 420px; top: 68px; }
  .identity .person-name { font-size: 26px; letter-spacing: 0.5px; }
  .identity .person-title { font-size: 17px; color: var(--ink-grey); margin-top: 4px; }
  .phones { left: 460px; top: 166px; font-size: 19px; line-height: 1.35; }
  .online { left: 330px; top: 284px; font-size: 18px; line-height: 1.45; }
</style>
</head>
<body>
<main class="canvas">
  <section class="card card-back" aria-label="Card back">
    <div class="wordmark">
      <span class="wordmark-square"></span>
      <span class="wordmark-name">Amber Hollow Productions</span>
    </div>
    <p class="web">www.amberhollowproductions.com</p>
  </section>

  <section class="card card-front" aria-label="Card front">
    <div class="band"></div>
    <svg class="corner-strip" viewBox="0 0 700 40" preserveAspectRatio="none" aria-hidden="true">
      <polygon points="40,40 60,22 600,0 700,0 700,40" fill="var(--brand-blue)"/>
    </svg>
    <div class="wordmark">
      <span class="wordmark-square"></span>
      <span class="wordmark-name">Amber Hollow Productions</span>
    </div>
    <div class="contact-block identity">
      <p class="person-name">YOUR NAME</p>
      <p class="person-title">Title</p>
    </div>
    <div class="contact-block phones">
      <p>P : 0987 654321</p>
      <p>C : 0987 654321</p>
    </div>
    <div class="contact-block online">
      <p>E : info@amberhollowproductions.com</p>
      <p>W: www.amberhollowproductions.com</p>
    </div>
  </section>
</main>
</body>
</html>
```